Upmarket Bathroom and Kitchen ware supplier needs a classy business card design

We are a company based in Fiji, we sell plumbing ware (Kitchen and bathroom taps, Basins,showers, toilets etc) through up market show rooms to individuals and directly through Architects and designers of resorts and holiday houses for new builds and renovations. we are wanting to upgrade our over all look and brand. we are starting with a new logo but will be rebranding the whole business. This project is for a business card design for my management and tales team I would like it to be dark, classy and interesting

Target Market(s)

Resort directors and Management, High end holiday home owners

Contact Information for Business Card

Gavin Threlkeld
Director
+64219473518

Colors

Designer to choose colors to be used in the design.

Requirements
Must have
• Must have an upmarket appearance I like darker charcoal shades but will be guided by the designers
• Please any catch phrases like "Crafting remarkable living rooms" this belongs tpo one of our suppliers so can not be used.
Nice to have
• Double sided, so front dedicated to logo provided and back info about the business and the person.

```html
<!DOCTYPE html>
<html lang="en">
<head>
<meta charset="utf-8">
<title>Velmora Interiors – Business Card</title>
<link href="https://fonts.googleapis.com/css2?family=Montserrat:wght@300;400;500&display=swap" rel="stylesheet">
<style>
  :root {
    --backdrop: #d9d9d8;
    --card: #2a2a2b;
    --card-edge: #f2f2f0;
    --ink: #f4f4f2;
    --ink-soft: #b9b9b7;
    --rule: #6b6b6b;
    --pattern-dark: #232324;
    --pattern-light: #4a4a4b;
  }
  * { box-sizing: border-box; margin: 0; padding: 0; }
  html, body {
    width: 1200px; height: 801px; overflow: hidden;
    background: var(--backdrop);
    font-family: "Montserrat", sans-serif;
  }
  .sheet {
    width: 1200px; height: 801px;
    display: flex; align-items: center; justify-content: center; gap: 44px;
  }
  .card {
    width: 532px; height: 304px;
    background: var(--card);
    border: 2px solid var(--card-edge);
    border-radius: 3px;
    position: relative;
    overflow: hidden;
    box-shadow: 0 14px 30px rgba(0,0,0,0.22);
  }

  /* Front */
  .card-front { display: flex; align-items: center; padding: 0 36px; }
  .brand { display: flex; align-items: center; gap: 10px; flex-shrink: 0; }
  .brand-dot {
    width: 28px; height: 28px; border: 1.5px solid var(--ink); border-radius: 50%;
    flex-shrink: 0;
  }
  .brand-name { color: var(--ink); font-weight: 300; line-height: 1.3; white-space: nowrap; }
  .brand-name .primary { display: block; font-size: 16px; letter-spacing: 6px; }
  .brand-name .secondary { display: block; font-size: 7px; letter-spacing: 4.5px; color: var(--ink-soft); padding-left: 2px; }
  .divider { width: 1px; height: 74px; background: var(--rule); margin: 0 24px; flex-shrink: 0; }
  .person { color: var(--ink); white-space: nowrap; }
  .person-name { font-size: 17px; font-weight: 500; letter-spacing: 1px; text-transform: uppercase; }
  .person-role { font-size: 12px; font-weight: 300; color: var(--ink-soft); margin-top: 3px; }
  .person-phone {
    display: flex; align-items: center; gap: 7px;
    font-size: 12px; font-weight: 300; color: var(--ink-soft); margin-top: 5px;
  }
  .person-phone svg { width: 11px; height: 11px; fill: var(--ink); }

  /* Back */
  .card-back .pattern {
    position: absolute; inset: 0;
    background: linear-gradient(120deg, var(--pattern-dark) 10%, #303031 45%, var(--pattern-light) 100%);
  }
  .back-mark {
    position: absolute; right: 34px; top: 50%; transform: translateY(-50%);
    display: flex; align-items: center; gap: 8px;
    color: var(--ink); font-weight: 300; font-size: 12px; letter-spacing: 4px;
  }
  .back-mark .brand-dot { width: 22px; height: 22px; }
</style>
</head>
<body>
  <main class="sheet">
    <section class="card card-front" aria-label="Business card front">
      <div class="brand">
        <span class="brand-dot"></span>
        <span class="brand-name">
          <span class="primary">VELMORA</span>
          <span class="secondary">INTERIORS</span>
        </span>
      </div>
      <div class="divider"></div>
      <div class="person">
        <p class="person-name">Gavin Threlkeld</p>
        <p class="person-role">Director</p>
        <p class="person-phone">
          <svg viewBox="0 0 24 24" aria-hidden="true"><path d="M6.6 10.8a15.1 15.1 0 0 0 6.6 6.6l2.2-2.2a1 1 0 0 1 1-.25 11.4 11.4 0 0 0 3.6.57 1 1 0 0 1 1 1V20a1 1 0 0 1-1 1A17 17 0 0 1 3 4a1 1 0 0 1 1-1h3.5a1 1 0 0 1 1 1c0 1.25.2 2.45.57 3.570a1 1 0 0 1-.25 1z"/></svg>
          +64219473518
        </p>
      </div>
    </section>

    <section class="card card-back" aria-label="Business card back">
      <div class="pattern" role="img" aria-label="Repeating brand monogram pattern fading from dark to light grey"></div>
      <div class="back-mark">
        <span class="brand-dot"></span>
        <span>VELMORA</span>
      </div>
    </section>
  </main>
</body>
</html>
```